Business Card for By Karel Voss

Looking to have a business card designed for my lifestyle and fitness company. My company offers personal training, online programming and nutrition advice based out of London, United Kingdom.

I'd like to see modern, sleek designs, focusing on black, matte black or matte grey. Design doesn't need to be overly descriptive as this will also be used as a personal business card. I've included my logo.

Please note that my company is no longer called "Fitness by Karel Voss" but instead "By Karel Voss", this is because of my other ventures. Therefore please don't use the "fitness by karel voss" text.

information about my company can be found at www.bykarelvoss.com

Company is also based out of Leeds (United Kingdom) & Perth (Australia) this could be reflected on the card.

Industry/Entity Type

Business

Contact Information for Business Card

Karel Voss
+44 7382 615027
karel@bykarelvoss.com
www.bykarelvoss.com

Font styles to use
Sans Serif

Requirements
Must have
• All contact details and inclusion of my logo.

```html
<!DOCTYPE html>
<html lang="en">
<head>
<meta charset="utf-8">
<title>By Karel Voss — Business Card</title>
<link href="https://fonts.googleapis.com/css2?family=Lato:wght@400;700&display=swap" rel="stylesheet">
<style>
  :root {
    --page: #e4e4e2;
    --card: #231f20;
    --ink: #ffffff;
    --rule: #d9d9d9;
  }
  * { box-sizing: border-box; margin: 0; padding: 0; }
  html, body {
    width: 1200px; height: 1000px; overflow: hidden;
    background: var(--page);
    font-family: "Lato", Arial, sans-serif;
    color: var(--ink);
  }
  .card {
    position: absolute; left: 220px;
    width: 760px; height: 434px;
    background: var(--card);
    border-radius: 42px;
    box-shadow: 0 6px 18px rgba(0,0,0,.18);
  }
  .card--front { top: 44px; }
  .card--back { top: 522px; }

  .brand {
    position: absolute; display: flex; flex-direction: column; align-items: center;
    font-weight: 700; color: var(--ink); letter-spacing: 2px; text-transform: uppercase;
  }
  .brand__dot { width: 46px; height: 46px; border-radius: 50%; background: var(--ink); }
  .card--front .brand { left: 0; right: 0; top: 120px; gap: 26px; font-size: 44px; }
  .card--back .brand { left: 28px; width: 215px; top: 120px; gap: 22px; font-size: 30px; text-align: center; line-height: 1.15; }

  .contact { position: absolute; right: 29px; text-align: right; white-space: nowrap; }
  .contact__name { top: 86px; font-size: 36px; font-weight: 400; }
  .contact__row { display: flex; align-items: center; gap: 24px; font-size: 25px; }
  .contact__row svg { width: 20px; height: 20px; fill: var(--ink); }
  .contact__phone { top: 208px; }
  .contact__email { top: 250px; }
  .contact__web { top: 334px; font-size: 21px; }
  .contact__cities { top: 372px; font-size: 16px; }

  .rule { position: absolute; right: 29px; height: 2px; background: var(--rule); }
  .rule--top { top: 179px; width: 443px; }
  .rule--bottom { top: 314px; width: 479px; }
</style>
</head>
<body>
  <section class="card card--front" aria-label="Card front">
    <div class="brand">
      <span class="brand__dot"></span>
      <span class="brand__name">By Karel Voss</span>
    </div>
  </section>

  <section class="card card--back" aria-label="Card back">
    <div class="brand">
      <span class="brand__dot"></span>
      <span class="brand__name">By Karel<br>Voss</span>
    </div>

    <h1 class="contact contact__name">Karel Voss</h1>
    <div class="rule rule--top"></div>

    <p class="contact contact__row contact__phone">
      <span>+44 7382 615027</span>
      <svg viewBox="0 0 24 24" aria-hidden="true"><path d="M6.6 10.8a15.1 15.1 0 0 0 6.6 6.6l2.2-2.2a1 1 0 0 1 1-.25 11.4 11.4 0 0 0 3.6.57 1 1 0 0 1 1 1V20a1 1 0 0 1-1 1A17 17 0 0 1 3 4a1 1 0 0 1 1-1h3.5a1 1 0 0 1 1 1c0 1.25.2 2.450.57 3.57a1 1 0 0 1-.25 1z"/></svg>
    </p>
    <p class="contact contact__row contact__email">
      <span>karel@bykarelvoss.com</span>
      <svg viewBox="0 0 24 24" aria-hidden="true"><path d="M2 5h20v14H2z M3.5 6.5v.4L12 13l8.5-6.1v-.4z" fill-rule="evenodd"/></svg>
    </p>

    <div class="rule rule--bottom"></div>

    <p class="contact contact__web">www.bykarelvoss.com</p>
    <p class="contact contact__cities">Leeds (United Kingdom) &amp; Perth (Australia)</p>
  </section>
</body>
</html>
```